Quillfern Nightclub Flyer (Updated)

Flyer for facebook, square is fine, or rectangular. Here is the text:
QUILLFERN
Nightclub + Lounge
presents

SPLIT DECK WEDNESDAY
Nov 29 2018

CLUB FLOOR:
GORDY B2B RALPH
THEODORE BRUSKVIK

LOUNGE:
OTIS B2B HALF TIDE
COPPER FENWICK

Powered by HALVERN Acoustics
4716 Larchmere Avenue 21+ 9pm-2am
quillfernvenue-example.com for VIP booth inquiries

Target Market(s)

Nightclub

Industry/Entity Type

Night Club

Font styles to use
Sans Serif

Colors

Designer to choose colors to be used in the design.

Requirements
Must have
• All the text listed, and plz keep the theme of the attached files. We want to stay consistent with the Quillfern brand
Nice to have
• Try to stay with the theme from the attachments
Should not have
• Dont' stray to far from the general theme we have from the attachments

```html
<!DOCTYPE html>
<html lang="en">
<head>
<meta charset="utf-8">
<title>Quillfern Nightclub + Lounge – Split Deck Wednesday</title>
<link rel="stylesheet" href="https://fonts.googleapis.com/css2?family=Source+Sans+3:wght@400;600&display=swap">
<style>
  :root {
    --page: #ffffff;
    --ink: #111010;
    --white: #ffffff;
    --gold: #c9985c;
    --gold-light: #e8c68f;
    --gold-dark: #8a5f2e;
    --label-grey: #4d4d4d;
    --rule-grey: #8c8c8c;
  }
  * { margin: 0; padding: 0; box-sizing: border-box; }
  html, body {
    width: 1200px;
    height: 1000px;
    overflow: hidden;
    background: var(--page);
    font-family: "Source Sans 3", sans-serif;
  }
  .flyer {
    position: absolute;
    left: 8px;
    top: 148px;
    width: 1188px;
    height: 669px;
    background: var(--ink);
    overflow: hidden;
  }
  .brand {
    position: absolute;
    left: 30px;
    top: 36px;
    width: 298px;
    text-align: center;
    color: var(--white);
  }
  .brand__name {
    font-size: 54px;
    font-weight: 400;
    letter-spacing: 1px;
    line-height: 1;
  }
  .brand__tagline {
    margin-top: 8px;
    font-size: 17px;
    letter-spacing: 3px;
    line-height: 22px;
  }
  .ornament {
    position: absolute;
    left: 0;
    bottom: 0;
    width: 372px;
    height: 404px;
    border-top-right-radius: 100% 100%;
    background: radial-gradient(circle at 0% 100%, var(--gold-light) 0%, var(--gold) 35%, var(--gold-dark) 65%, rgba(138,95,46,0) 100%);
    opacity: 0.85;
  }
  .date-box {
    position: absolute;
    left: 380px;
    top: 168px;
    width: 115px;
    height: 52px;
    border: 2px solid var(--gold);
    color: var(--gold);
    font-size: 27px;
    line-height: 48px;
    text-align: center;
  }
  .event-title {
    position: absolute;
    left: 530px;
    top: 172px;
    color: var(--white);
    font-size: 35px;
    letter-spacing: 0.5px;
    line-height: 40px;
  }
  .event-rule {
    position: absolute;
    left: 517px;
    top: 212px;
    width: 594px;
    height: 14px;
  }
  .lineup {
    position: absolute;
    left: 340px;
    width: 600px;
  }
  .lineup--club { top: 276px; }
  .lineup--lounge { top: 392px; }
  .lineup__label {
    position: absolute;
    left: 0;
    width: 225px;
    text-align: right;
    color: var(--label-grey);
    font-size: 23px;
    letter-spacing: 4px;
    line-height: 30px;
  }
  .lineup__acts { position: absolute; left: 246px; list-style: none; }
  .lineup__act {
    position: relative;
    padding-left: 23px;
    color: var(--white);
    font-size: 25px;
    letter-spacing: -0.6px;
    line-height: 30px;
    margin-bottom: 10px;
  }
  .lineup__act::before {
    content: "";
    position: absolute;
    left: 2px;
    top: 14px;
    width: 4px;
    height: 4px;
    border-radius: 50%;
    background: var(--white);
  }
  .venue-info {
    position: absolute;
    left: 469px;
    top: 540px;
    width: 540px;
    height: 94px;
    border-top: 1px solid var(--rule-grey);
    border-bottom: 1px solid var(--rule-grey);
    padding: 6px 0 0 4px;
    color: var(--gold);
  }
  .venue-info__line { font-size: 18px; line-height: 28px; }
  .venue-info__web { font-size: 14px; letter-spacing: 0.8px; line-height: 26px; text-transform: uppercase; }
</style>
</head>
<body>
  <main class="flyer">
    <header class="brand">
      <div class="brand__name">QUILLFERN</div>
      <div class="brand__tagline">NIGHTCLUB + LOUNGE<br>PRESENTS</div>
    </header>

    <div class="ornament" role="img" aria-label="Gold ornamental mandala decoration"></div>

    <div class="date-box">NOV 29</div>
    <h1 class="event-title" style="font-weight:400">SPLIT DECK WEDNESDAY</h1>
    <svg class="event-rule" viewBox="0 0 594 14" aria-hidden="true">
      <defs>
        <linearGradient id="ruleGold" x1="0" x2="1">
          <stop offset="0" stop-color="#b88544"/>
          <stop offset="0.5" stop-color="#e8c68f"/>
          <stop offset="1" stop-color="#b88544"/>
        </linearGradient>
      </defs>
      <rect x="0" y="6" width="578" height="2" fill="url(#ruleGold)"/>
      <circle cx="586" cy="7" r="4" fill="none" stroke="#c9985c" stroke-width="1.5"/>
    </svg>

    <section class="lineup lineup--club">
      <div class="lineup__label">CLUB FLOOR:</div>
      <ul class="lineup__acts">
        <li class="lineup__act">GORDY B2B RALPH</li>
        <li class="lineup__act">THEODORE BRUSKVIK</li>
      </ul>
    </section>

    <section class="lineup lineup--lounge">
      <div class="lineup__label">LOUNGE:</div>
      <ul class="lineup__acts">
        <li class="lineup__act">OTIS &nbsp;B2B &nbsp;HALF TIDE</li>
        <li class="lineup__act">COPPER FENWICK</li>
      </ul>
    </section>

    <footer class="venue-info">
      <div class="venue-info__line">Powered by HALVERN Acoustics</div>
      <div class="venue-info__line">4716 Larchmere Avenue 21+9PM-2AM</div>
      <div class="venue-info__web">quillfernvenue-example.com for VIP booth inquiries</div>
    </footer>
  </main>
</body>
</html>
```